Heating and Cooling Company mobile website

We need a website specifically designed for a viewing on a mobile device.

We serve the northern New Jersey heating, cooling and electrical residential market.

The goal is the drive traffic to the site by using Brindle Pay Per click. People will be searching for an HVAC contractor, and they land on our page. They need to get key info quickly without all the clutter of a desktop type of site.

Target Market(s)

Homeowners

Industry/Entity Type

Hvac

Coding

Coded - Design and coding required

Number of Pages Required

5+ page

Font styles to use
Serif

Requirements
Must have
• View attachments to see samples of the desktop version. It must have a similar color scheme
• The copy of the website is also attached
Nice to have
• Would like it to have a sort of Talvix feel to it. Make it seem like its an app that people are using and that its exciting to be on the website. It would be nice to have a page where customers can book appointments

```html
<!DOCTYPE html>
<html lang="en">
<head>
<meta charset="utf-8">
<title>Warmhaven Services – Heating &amp; Cooling</title>
<link rel="stylesheet" href="https://fonts.googleapis.com/css2?family=Cinzel:wght@400;700&family=Cormorant+Garamond:ital,wght@1,600&family=Lato:wght@400;700;900&family=Oswald:wght@400;500&display=swap">
<style>
  :root {
    --orange: #f7941d;
    --orange-dark: #e07f0c;
    --red: #9b2335;
    --red-dark: #7d1a2a;
    --white: #ffffff;
    --cream: #f3eee6;
    --ink: #5a1d24;
  }
  * { box-sizing: border-box; margin: 0; padding: 0; }
  html, body { width: 1200px; height: 3700px; overflow: hidden; background: var(--white); }
  .page { width: 1200px; height: 3700px; display: flex; flex-direction: column; font-family: "Lato", sans-serif; }

  /* Header */
  .site-header { height: 360px; position: relative; background: var(--white); }
  .top-bar { height: 130px; background: var(--orange); display: flex; justify-content: space-between; align-items: center; padding: 0 130px; }
  .icon-btn { width: 84px; height: 84px; background: var(--red); border-radius: 10px; display: flex; align-items: center; justify-content: center; }
  .brand { position: absolute; left: 0; right: 0; top: 150px; text-align: center; }
  .brand-name { font-family: "Cinzel", serif; font-weight: 700; font-size: 88px; color: var(--red); line-height: 1; letter-spacing: 2px; }
  .brand-sub { font-family: "Cinzel", serif; font-weight: 700; font-size: 88px; color: var(--red); line-height: 1.05; letter-spacing: 2px; }

  /* Hero */
  .hero { height: 617px; position: relative; overflow: hidden; }
  .hero-photo { position: absolute; inset: 0; background: linear-gradient(100deg, #ece7df 0%, #ddd5ca 45%, #c9c0b4 70%, #4a4648 100%); }
  .hero-tagline { position: absolute; left: 120px; top: 210px; font-family: "Cinzel", serif; font-size: 50px; line-height: 1.25; color: var(--ink); }
  .hero-dots { position: absolute; left: 120px; bottom: 40px; display: flex; gap: 18px; }
  .hero-dots span { width: 16px; height: 16px; border-radius: 50%; background: #9a9a9a; }
  .hero-dots span.active { background: var(--orange); }

  /* Open */
  .open-hours { height: 488px; background: var(--white); display: flex; flex-direction: column; align-items: center; padding-top: 70px; }
  .ribbon { position: relative; background: var(--red); color: var(--white); font-family: "Oswald", sans-serif; font-weight: 500; font-size: 60px; padding: 8px 70px; border: 6px solid var(--orange); }
  .quote { margin-top: 60px; width: 900px; text-align: center; font-family: "Cormorant Garamond", serif; font-style: italic; font-weight: 600; font-size: 50px; line-height: 1.25; color: var(--ink); letter-spacing: 1px; }

  /* Call */
  .call-now { height: 308px; background: var(--orange); display: flex; flex-direction: column; align-items: center; justify-content: center; color: var(--white); font-family: "Oswald", sans-serif; }
  .call-title { font-size: 96px; font-weight: 500; line-height: 1.1; }
  .call-number { display: flex; align-items: center; gap: 24px; font-size: 84px; font-weight: 400; line-height: 1.2; }

  /* Services */
  .services { height: 925px; display: grid; grid-template-columns: 1fr 1fr; padding: 90px 120px 40px; row-gap: 60px; }
  .service { display: flex; flex-direction: column; align-items: center; }
  .service-label { margin-top: 30px; font-weight: 700; font-size: 50px; color: var(--red); }

  /* Social */
  .social { height: 154px; background: var(--white); position: relative; display: flex; justify-content: center; align-items: center; }
  .social-band { position: absolute; left: 130px; right: 130px; top: 12px; bottom: 0; background: var(--orange); clip-path: polygon(0 0, 100% 0, 96% 50%, 100% 100%, 0 100%, 4% 50%); }
  .social-links { position: relative; display: flex; gap: 40px; }
  .social-link { display: flex; align-items: center; gap: 22px; color: var(--white); font-size: 54px; font-weight: 700; }
  .social-mark { width: 80px; height: 80px; background: var(--red); border-radius: 12px; }

  /* Contact */
  .contact { height: 771px; background: var(--red); color: var(--white); text-align: center; padding-top: 80px; }
  .contact h2 { font-family: "Cinzel", serif; font-weight: 400; font-size: 84px; color: var(--orange); }
  .contact hr { width: 900px; margin: 20px auto 40px; border: 0; border-top: 3px solid rgba(255,255,255,.55); }
  .contact-name { font-family: "Cinzel", serif; font-size: 70px; }
  .contact-address { font-size: 46px; margin-top: 10px; }
  .licenses { margin-top: 90px; font-size: 46px; line-height: 1.6; }
  .licenses b { color: var(--orange); font-weight: 400; }

  /* Footer */
  .site-footer { height: 77px; background: var(--orange); color: var(--white); display: flex; align-items: center; justify-content: center; font-size: 30px; }
</style>
</head>
<body>
<div class="page">

  <header class="site-header">
    <div class="top-bar">
      <div class="icon-btn" aria-label="Call">
        <svg width="48" height="48" viewBox="0 0 24 24"><path fill="#fff" d="M6.6 10.8a15 15 0 0 0 6.6 6.6l2.2-2.2a1 1 0 0 1 1-.25 11.4 11.4 0 0 0 3.6.57 1 1 0 0 1 1 1V20a1 1 0 0 1-1 1A17 17 0 0 1 3 4a1 1 0 0 1 1-1h3.5a1 1 0 0 1 1 1c0 1.25.2 2.45.57 3.570a1 1 0 0 1-.25 1z"/></svg>
      </div>
      <div class="icon-btn" aria-label="Menu">
        <svg width="50" height="40" viewBox="0 0 50 40"><rect y="2" width="50" height="6" rx="3" fill="#fff"/><rect y="17" width="50" height="6" rx="3" fill="#fff"/><rect y="32" width="50" height="6" rx="3" fill="#fff"/></svg>
      </div>
    </div>
    <div class="brand">
      <div class="brand-name">Warmhaven</div>
      <div class="brand-sub">Services</div>
    </div>
  </header>

  <section class="hero">
    <div class="hero-photo" role="img" aria-label="Smiling family beside the company's service van"></div>
    <p class="hero-tagline">The Best Way To<br>Live In New Jersey<br>Is With Comfort!</p>
    <div class="hero-dots"><span class="active"></span><span></span><span></span><span></span></div>
  </section>

  <section class="open-hours">
    <div class="ribbon">Yes We Are Open</div>
    <p class="quote">"Seriously, don't be afraid to call at any time, we live for this, just give us a min to get some coffee on the way over"</p>
  </section>

  <section class="call-now">
    <div class="call-title">Call Us Now</div>
    <div class="call-number">
      <svg width="78" height="78" viewBox="0 0 40 40"><circle cx="20" cy="20" r="17" fill="none" stroke="#fff" stroke-width="3"/><path fill="#fff" d="M14 12.5c1-.8 2-.6 2.5.3l1.6 3c.4.8.1 1.5-.6 2l-1 .8c.8 2 2.3 3.6 4.3 4.5l.9-1c.6-.7 1.3-.9 2.1-.5l2.9 1.7c.9.5 1 1.6.2 2.5-1.6 1.8-3.6 2.2-6 1-3.6-1.8-6.3-4.7-7.7-8.5-.8-2.4-.5-4.300 .8-5.8z"/></svg>
      973-555-0148
    </div>
  </section>

  <section class="services">
    <div class="service">
      <svg width="300" height="230" viewBox="0 0 300 230">
        <path d="M40 20 Q150 0 260 20 Q290 70 270 115 Q290 160 260 210 Q150 230 40 210 Q10 160 30 115 Q10 70 40 20z" fill="#fff" stroke="var(--orange)" stroke-width="6"/>
        <g stroke="var(--red)" stroke-width="7" fill="none" stroke-linecap="round">
          <rect x="105" y="95" width="90" height="80" rx="8"/>
          <line x1="128" y1="100" x2="128" y2="170"/><line x1="150" y1="100" x2="150" y2="170"/><line x1="172" y1="100" x2="172" y2="170"/>
          <path d="M125 80c-6-8 6-14 0-22M150 80c-6-8 6-14 0-22M175 80c-6-8 6-14 0-22"/>
        </g>
      </svg>
      <div class="service-label">Heating</div>
    </div>
    <div class="service">
      <svg width="300" height="230" viewBox="0 0 300 230">
        <path d="M40 20 Q150 0 260 20 Q290 70 270 115 Q290 160 260 210 Q150 230 40 210 Q10 160 30 115 Q10 70 40 20z" fill="#fff" stroke="var(--orange)" stroke-width="6"/>
        <g stroke="var(--red)" stroke-width="8" stroke-linecap="round">
          <line x1="150" y1="65" x2="150" y2="165"/><line x1="107" y1="90" x2="193" y2="140"/><line x1="107" y1="140" x2="193" y2="90"/>
          <path d="M138 75l12 10 12-10M138 155l12-10 12 10" fill="none"/>
        </g>
      </svg>
      <div class="service-label">Air conditioning</div>
    </div>
    <div class="service">
      <svg width="300" height="230" viewBox="0 0 300 230">
        <path d="M40 20 Q150 0 260 20 Q290 70 270 115 Q290 160 260 210 Q150 230 40 210 Q10 160 30 115 Q10 70 40 20z" fill="#fff" stroke="var(--orange)" stroke-width="6"/>
        <circle cx="150" cy="115" r="50" fill="var(--red)"/>
        <rect x="128" y="100" width="40" height="30" rx="6" fill="#fff"/>
        <rect x="168" y="105" width="18" height="6" fill="#fff"/><rect x="168" y="119" width="18" height="6" fill="#fff"/>
        <rect x="108" y="111" width="22" height="8" fill="#fff"/>
      </svg>
      <div class="service-label">Electrical</div>
    </div>
    <div class="service">
      <svg width="300" height="230" viewBox="0 0 300 230">
        <path d="M40 20 Q150 0 260 20 Q290 70 270 115 Q290 160 260 210 Q150 230 40 210 Q10 160 30 115 Q10 70 40 20z" fill="#fff" stroke="var(--orange)" stroke-width="6"/>
        <circle cx="150" cy="115" r="50" fill="var(--red)"/>
        <g fill="#fff">
          <path d="M150 115 L140 72 Q150 66 162 72z"/>
          <path d="M150 115 L190 128 Q190 140 180 147z"/>
          <path d="M150 115 L118 146 Q108 138 106 126z"/>
          <circle cx="150" cy="115" r="8"/>
        </g>
      </svg>
      <div class="service-label">Ventilation</div>
    </div>
  </section>

  <section class="social">
    <div class="social-band"></div>
    <div class="social-links">
      <div class="social-link"><span class="social-mark"></span>Chatter</div>
      <div class="social-link"><span class="social-mark"></span>Reelbox</div>
    </div>
  </section>

  <section class="contact">
    <h2>Contact Details</h2>
    <hr>
    <div class="contact-name">WARMHAVEN SERVICES</div>
    <div class="contact-address">P.O Box 418 Larkwood NJ 07990</div>
    <div class="licenses">
      Electrical License Number <b>40291</b><br>
      Contractors License Number <b>13VH0921384</b><br>
      Master HVAC License <b>582</b>
    </div>
  </section>

  <footer class="site-footer">© Copyright 2017 WARMHAVEN SERVICES. All Rights Reserved.</footer>

</div>
</body>
</html>
```